luxury contemporary fashion website needs simple, elegant flowchart to describe the buying and selli

* Luxury, resale, preloved items are sold on this online platform
*Horizontal, simple, flowchart with 5 steps in 'friendly' font with a simple emoticon/ picture for each step
*To be positioned in the 'How we work' tab of the webpage to explain in a very simple manner the buying and selling process for the customers.
*Attached is a very rudimentary mock-up of what we would like included and an idea of a project similar to what we desire
* to confirm the text for each step, we have also attached a word file below

Industry/Entity Type

Fashion

Font styles to use
Sans Serif

Colors
86cfc6
cfeae6

Requirements
Must have
• Simple drawing / shape after each point In the closest to 'duck egg blue' fill colour you can find with a black outline

```html
<!DOCTYPE html>
<html lang="en">
<head>
<meta charset="utf-8">
<title>How We Work</title>
<link rel="stylesheet" href="https://fonts.googleapis.com/css2?family=Source+Sans+3:wght@400;600&display=swap">
<style>
  :root {
    --duck-egg: #86cfc6;
    --duck-egg-light: #cfeae6;
    --ink: #1a1a1a;
    --paper: #ffffff;
  }
  * { box-sizing: border-box; margin: 0; padding: 0; }
  html, body { width: 1200px; height: 857px; overflow: hidden; background: var(--paper); }
  body { font-family: "Source Sans 3", sans-serif; color: var(--ink); position: relative; }
  .flow-graphics { position: absolute; left: 0; top: 0; }
  .step { position: absolute; top: 448px; width: 190px; }
  .step-title { font-size: 17px; font-weight: 400; letter-spacing: 0.1px; line-height: 20px; text-transform: uppercase; white-space: nowrap; }
  .step-text { font-size: 11px; line-height: 14.3px; }
  .step-text .indent { padding-left: 10px; display: inline-block; }
  .step-button {
    position: absolute; top: 101px; left: 0;
    width: 83px; height: 30px;
    background: var(--duck-egg); color: var(--ink);
    border: 1px solid var(--ink); border-radius: 14px 14px 4px 4px;
    font-family: Arial, sans-serif; font-size: 9.5px; letter-spacing: 0.2px;
    display: flex; align-items: center; justify-content: center;
  }
</style>
</head>
<body>

<svg class="flow-graphics" width="1200" height="857" viewBox="0 0 1200 857" aria-hidden="true">
  <g fill="var(--duck-egg)" stroke="var(--ink)" stroke-width="1.5">
    <circle cx="106.5" cy="384.5" r="54"/>
    <circle cx="338" cy="384.5" r="54"/>
    <circle cx="566" cy="384.5" r="54"/>
    <circle cx="798" cy="384.5" r="54"/>
    <circle cx="995" cy="384.5" r="54"/>
    <circle cx="1144" cy="314" r="24.5"/>
    <circle cx="1144" cy="439" r="24.5"/>
    <path d="M1057 341 L1088 323 L1084 316 L1104 318 L1095 336 L1092 330 L1061 348 Z" stroke-linejoin="round"/>
    <path d="M1062 417 L1092 430 L1089 437 L1109 435 L1098 418 L1095 424 L1065 410 Z" stroke-linejoin="round"/>
  </g>

  <!-- clipboard checklist -->
  <rect x="83" y="355" width="47" height="61" rx="7" fill="var(--duck-egg-light)" stroke="var(--ink)" stroke-width="3"/>
  <g fill="none" stroke="var(--ink)" stroke-width="3" stroke-linecap="round" stroke-linejoin="round">
    <path d="M92 372 l3 3 l6 -6 M92 386 l3 3 l6 -6 M92 400 l3 3 l6 -6"/>
    <path d="M106 373 h14 M106 387 h14 M106 401 h14"/>
  </g>
  <path d="M96 360 h21 v-3 a5 5 0 0 0 -5 -5 a5 5 0 0 0 -10 0 a5 5 0 0 0 -6 5 z" fill="var(--duck-egg-light)" stroke="var(--ink)" stroke-width="1.5"/>

  <!-- basket -->
  <g fill="var(--duck-egg-light)" stroke="var(--ink)" stroke-width="1.5" stroke-linejoin="round">
    <path d="M312 348 l10 24 h6 l-8 -26 z"/>
    <circle cx="336" cy="367" r="7"/>
    <path d="M349 372 l8 -12 l6 4 l-8 10 z"/>
    <path d="M307 382 h66 v8 h-4 l-6 31 h-46 l-6 -31 h-4 z"/>
  </g>
  <g fill="var(--ink)">
    <rect x="329" y="396" width="4" height="18" rx="2"/>
    <rect x="337" y="396" width="4" height="18" rx="2"/>
    <rect x="345" y="396" width="4" height="18" rx="2"/>
  </g>

  <!-- document with magnifier -->
  <g stroke="var(--ink)" stroke-width="2" fill="none" stroke-linejoin="round">
    <path d="M557 348 h28 l10 10 v54 h-38 z" fill="var(--duck-egg-light)"/>
    <path d="M564 362 h22 M564 370 h24 M564 378 h24 M564 386 h24"/>
    <circle cx="561" cy="395" r="14" fill="var(--duck-egg)" stroke-width="2.5"/>
    <path d="M551 405 l-22 14" stroke-linecap="round" stroke-width="2.5"/>
  </g>

  <!-- delivery truck -->
  <g fill="var(--duck-egg-light)" stroke="var(--ink)" stroke-width="1.5" stroke-linejoin="round">
    <rect x="770" y="360" width="42" height="42" rx="3"/>
    <path d="M815 371 h12 l12 16 v15 h-24 z"/>
  </g>
  <path d="M758 373 h10 M755 379 h13 M760 385 h8" stroke="var(--ink)" stroke-width="2.5"/>
  <g fill="var(--duck-egg-light)" stroke="var(--ink)" stroke-width="2.5">
    <circle cx="786" cy="402" r="7"/>
    <circle cx="829" cy="402" r="7"/>
  </g>
  <circle cx="790" cy="376" r="10" fill="var(--duck-egg)" stroke="var(--ink)" stroke-width="2.5"/>

  <!-- coins -->
  <g fill="var(--duck-egg-light)" stroke="var(--ink)" stroke-width="1.5">
    <ellipse cx="1003" cy="400" rx="15" ry="6"/>
    <ellipse cx="1003" cy="393" rx="15" ry="6"/>
    <ellipse cx="1003" cy="386" rx="15" ry="6"/>
    <ellipse cx="1003" cy="379" rx="15" ry="6"/>
    <ellipse cx="1003" cy="372" rx="15" ry="6"/>
    <ellipse cx="1003" cy="365" rx="15" ry="6"/>
    <ellipse cx="985" cy="403" rx="15" ry="6"/>
    <ellipse cx="985" cy="396" rx="15" ry="6"/>
    <ellipse cx="985" cy="389" rx="15" ry="6"/>
  </g>

  <!-- dollar sign -->
  <text x="1144" y="326" text-anchor="middle" fill="var(--duck-egg-light)" stroke="var(--ink)" stroke-width="1.2" font-family="Arial, sans-serif" font-weight="700" font-size="34">$</text>

  <!-- donation box -->
  <g fill="var(--duck-egg-light)" stroke="var(--ink)" stroke-width="1.5" stroke-linejoin="round">
    <rect x="1132" y="423" width="24" height="8" rx="2"/>
    <path d="M1134 435 h6 l4 3 l4 -3 h6 v14 a2 2 0 0 1 -2 2 h-16 a2 2 0 0 1 -2 -2 z"/>
  </g>
  <path d="M1144 432 v5" stroke="var(--ink)" stroke-width="2"/>
</svg>

<section class="step" style="left:40px; top:450px">
  <h2 class="step-title">Have Items to Sell?</h2>
  <p class="step-text">Brand Spanking or Nearly New<small>★★★</small></p>
  <a class="step-button" style="top:99px">CLICK HERE</a>
</section>

<section class="step" style="left:265px">
  <h2 class="step-title">PersonalCollection</h2>
  <p class="step-text">We Choose the Pieces We Know the<br>Velora Customers Will Love♥</p>
  <a class="step-button">CLICK HERE</a>
</section>

<section class="step" style="left:518px">
  <h2 class="step-title">We Prepare</h2>
  <p class="step-text">Your item for Sale with<br>thorough Authenticity &amp;<br>Condition checks... so you<br>don't have to ☺</p>
  <a class="step-button">CLICK HERE</a>
</section>

<section class="step" style="left:740px">
  <h2 class="step-title">Once Sold</h2>
  <p class="step-text">1) We Lovingly Prepare the item<br>2) Shipped via Tracked Servcies✈</p>
  <a class="step-button">CLICK HERE</a>
</section>

<section class="step" style="left:936px">
  <h2 class="step-title">Your Payment</h2>
  <p class="step-text">i) Pocket the Cash.<br>ii) Donate to Charity Full or<br><span class="indent">Partial Amount</span></p>
  <a class="step-button">CLICK HERE</a>
</section>

</body>
</html>
```